Bellwether Home Inspections

We need stationery for our new home inspection company. We inspect homes for people prior to purchasing to ensure the property is in good condition, as well as inspecting new homes to ensure they have been built to the appropriate standards. We are happy to look at combinations of colours. The use of a water mark would be good. Open to suggestions.

Industry/Entity Type

Home Inspection

```html
<!DOCTYPE html>
<html lang="en">
<head>
<meta charset="utf-8">
<title>Bellwether Home Inspections – Stationery</title>
<link href="https://fonts.googleapis.com/css2?family=Questrial&display=swap" rel="stylesheet">
<style>
:root{
  --bg:#e6e6e6;
  --paper:#ffffff;
  --brand:#0d6591;
  --brand-band:#1a7199;
  --brand-soft:#6f9fbd;
  --wash-pale:#dbe6ee;
  --wash-mid:#b9cddb;
  --wash-on-blue:#2f7aa3;
  --ink:#222a30;
  --flap:#ececec;
}
*{margin:0;padding:0;box-sizing:border-box}
html,body{width:1200px;height:752px;overflow:hidden}
body{background:var(--bg);font-family:"Questrial",sans-serif;color:var(--ink);position:relative}
.piece{position:absolute;background:var(--paper);overflow:hidden}
.brand{display:flex;align-items:center;gap:5px;color:var(--brand);line-height:1.05;white-space:nowrap}
.brand-dot{width:12px;height:12px;background:var(--brand);flex:none}
.brand--light{color:#fff}
.brand--light .brand-dot{background:#fff}
.wash{position:absolute}
.contact{display:flex;gap:14px;font-size:5.5px;align-items:flex-start;white-space:nowrap;line-height:1.25}
.contact span{display:flex;gap:4px;align-items:flex-start}
.contact svg{width:6px;height:6px;flex:none}

/* letterhead */
.letterhead{left:60px;top:52px;width:273px;height:394px}
.letterhead .brand{position:absolute;right:14px;top:18px;font-size:8px}
.letterhead .wash{left:70px;top:80px;width:140px;height:240px;background:linear-gradient(#f1f4f7,#f8f9fb)}
.letterhead .body-copy{position:absolute;left:28px;top:70px;width:215px;font-size:5.4px;line-height:1.38;text-align:justify;color:#333}
.letterhead .body-copy p{margin-bottom:6px}
.letterhead .signature{position:absolute;left:186px;top:258px;width:50px;height:16px;background:#e5e8f7}
.letterhead .signer{position:absolute;right:30px;top:274px;font-size:5.4px;text-align:right;line-height:1.3}
.letterhead .band-top{position:absolute;left:0;right:0;top:358px;height:5px;background:var(--brand-soft)}
.letterhead .band{position:absolute;left:0;right:0;top:363px;height:21px;background:var(--brand-band);color:#fff;padding:4px 0 0 28px}
.letterhead .contact{gap:12px}

/* folder */
.folder{left:400px;top:54px;width:268px;height:390px;background:var(--brand)}
.folder .brand--small{position:absolute;left:15px;top:20px;font-size:5.5px}
.folder .brand--small .brand-dot{width:8px;height:8px}
.folder .wash{left:0;top:60px;width:268px;height:256px;background:radial-gradient(ellipse at 50% 45%,var(--wash-on-blue),var(--brand) 75%)}
.folder .brand--main{position:absolute;left:30px;top:150px;font-size:17px;gap:10px}
.folder .brand--main .brand-dot{width:30px;height:30px}
.folder .contact{position:absolute;left:35px;top:370px;color:#fff;gap:16px}

/* pocket sheet */
.pocket{left:735px;top:58px;width:273px;height:392px}
.pocket .flap{position:absolute;left:17px;right:9px;top:0;height:54px;background:var(--flap);clip-path:polygon(0 0,100% 0,95% 100%,5% 100%)}
.pocket .wash{left:0;top:190px;width:200px;height:202px;background:radial-gradient(ellipse at 40% 40%,var(--wash-pale),rgba(255,255,255,0) 70%)}
.pocket .brand{position:absolute;left:6px;top:360px;font-size:5.5px}
.pocket .brand-dot{width:8px;height:8px}
.pocket .contact{position:absolute;left:68px;top:374px;color:var(--brand);gap:10px}

/* envelope front */
.env-front{left:65px;top:523px;width:295px;height:133px}
.env-front .brand{position:absolute;left:15px;top:15px;font-size:5.5px}
.env-front .brand-dot{width:10px;height:10px}
.env-front .wash{left:190px;top:30px;width:105px;height:103px;background:radial-gradient(ellipse at 60% 50%,var(--wash-mid),rgba(255,255,255,0) 70%)}
.env-front .note{position:absolute;left:93px;top:120px;font-size:5.5px;font-weight:700;letter-spacing:.1px;white-space:nowrap}

/* envelope back */
.env-back{left:390px;top:523px;width:295px;height:133px}
.env-back .flap{position:absolute;left:0;top:0;width:100%;height:54px;background:var(--brand);clip-path:polygon(0 0,100% 0,94% 100%,6% 100%)}

/* business cards */
.card-front{left:813px;top:481px;width:152px;height:89px;background:var(--brand)}
.card-front .wash{left:80px;top:10px;width:72px;height:79px;background:radial-gradient(ellipse at 60% 60%,var(--wash-on-blue),var(--brand) 70%)}
.card-front .brand{position:absolute;left:0;right:0;top:25px;flex-direction:column;font-size:7.5px;text-align:center;gap:4px}
.card-front .brand-dot{width:18px;height:18px}
.card-back{left:813px;top:589px;width:152px;height:89px}
.card-back .brand{position:absolute;left:7px;top:8px;font-size:5.5px}
.card-back .brand-dot{width:10px;height:10px}
.card-back .wash{left:82px;top:14px;width:70px;height:75px;background:radial-gradient(ellipse at 55% 55%,var(--wash-pale),rgba(255,255,255,0) 72%)}
.card-back .name{position:absolute;left:86px;top:32px;font-size:8.5px;color:var(--ink);line-height:1;white-space:nowrap}
.card-back .role{position:absolute;left:128px;top:42px;font-size:4px}
.card-back .lines{position:absolute;left:13px;top:47px;font-size:4px;color:var(--brand);line-height:1.1;white-space:nowrap}
.card-back .lines div{display:flex;gap:4px;align-items:flex-start;margin-bottom:3px}
.card-back .lines svg{width:5px;height:5px;flex:none}
</style>
</head>
<body>

<svg width="0" height="0" style="position:absolute">
  <defs>
    <symbol id="i-phone" viewBox="0 0 10 10"><path d="M2 1l2 2-1 1.5c.6 1.2 1.3 1.9 2.5 2.5L7 6l2 2-1.5 1.5C4.5 9 1 5.5.5 2.5z" fill="currentColor"/></symbol>
    <symbol id="i-mail" viewBox="0 0 10 10"><rect x="0" y="2" width="10" height="6.5" fill="currentColor"/><path d="M0 2l5 3.5L10 2" stroke="#fff" stroke-width=".8" fill="none"/></symbol>
    <symbol id="i-pin" viewBox="0 0 10 10"><path d="M5 0C3 0 1.5 1.5 1.5 3.5 1.5 6 5 10 5 10s3.5-4 3.5-6.5C8.5 1.5 7 0 5 0zm0 5a1.5 1.5 0 110-3 1.5 1.5 0 010 3z" fill="currentColor"/></symbol>
  </defs>
</svg>

<section class="piece letterhead">
  <div class="brand"><span class="brand-dot"></span><span>Bellwether<br>Home Inspections</span></div>
  <div class="wash" role="img" aria-label="Faint company watermark area"></div>
  <div class="body-copy">
    <p>Lorem Ipsum<br>Lorem Ipsum<br>Lorem Ipsum</p>
    <p>Lorem ipsum dolor sit amet, consectetur adipiscing elit. Donec at commodo dolor, in fermentum orci. Donec semper tristique justo, a rhoncus quam gravida sed. Pellentesque pretium erat vel ligula scelerisque dapibus. Phasellus non interdum urna, eget feugiat tellus. Vivamus bibendum sapien et sapien scelerisque, vitae egestas nisi egestas. Duis malesuada a nisi id sodales. Cras suscipit sem at felis rhoncus viverra nec quis mi. Fusce dapibus dolor ac cursus luctus. Suspendisse ullamcorper libero in dui ullamcorper tincidunt. Nam vel tincidunt tortor, eu tristique nisl. Nunc ut accumsan massa. Nulla viverra vel erat ac interdum. Integer lacinia semper tincidunt. Duis vestibulum eleifend diam, ut ultrices est faucibus ac. Proin lorem mi, porta eget interdum vel, cursus eget ligula. Donec fermentum, tortor non laoreet egestas, nulla diam volutpat urna, et pretium dui nibh at tortor. Aenean elementum egestas eros id rutrum. Nullam in lorem a massa laoreet consectetur. Integer molestie massa vel nisi volutpat dictum in in turpis.</p>
    <p>Lorem ipsum dolor sit amet, consectetur adipiscing elit. Donec at commodo dolor, in fermentum orci. Donec semper tristique justo, a rhoncus quam gravida sed. Pellentesque pretium erat vel ligula scelerisque dapibus. Phasellus non interdum urna, eget feugiat tellus. Vivamus bibendum sapien et sapien scelerisque, vitae egestas nisi egestas. Duis malesuada a nisi id sodales. Cras suscipit sem at felis rhoncus viverra nec quis mi. Fusce dapibus dolor ac cursus luctus. Suspendisse ullamcorper libero in dui ullamcorper tincidunt. Nam vel tincidunt tortor, eu tristique nisl.</p>
  </div>
  <div class="signature" role="img" aria-label="Handwritten signature"></div>
  <div class="signer">Daniel Reeve<br>Chief Executive Officer</div>
  <div class="band-top"></div>
  <div class="band">
    <div class="contact">
      <span><svg><use href="#i-phone"/></svg>210-555-0147</span>
      <span><svg><use href="#i-mail"/></svg>hello@bellwetherhome.com</span>
      <span><svg><use href="#i-pin"/></svg>412 Alder Lane<br>Westbrook, Fairmont 00412</span>
    </div>
  </div>
</section>

<section class="piece folder">
  <div class="wash" role="img" aria-label="Large faint company watermark area"></div>
  <div class="brand brand--light brand--small"><span class="brand-dot"></span><span>Bellwether<br>Home Inspections</span></div>
  <div class="brand brand--light brand--main"><span class="brand-dot"></span><span>Bellwether<br>Home Inspections</span></div>
  <div class="contact">
    <span><svg><use href="#i-phone"/></svg>210-555-0147</span>
    <span><svg><use href="#i-mail"/></svg>hello@bellwetherhome.com</span>
    <span><svg><use href="#i-pin"/></svg>412 Alder Lane<br>Westbrook, Fairmont 00412</span>
  </div>
</section>

<section class="piece pocket">
  <div class="flap"></div>
  <div class="wash" role="img" aria-label="Large faint company watermark area"></div>
  <div class="brand"><span class="brand-dot"></span><span>Bellwether<br>Home Inspections</span></div>
  <div class="contact">
    <span><svg><use href="#i-phone"/></svg>210-555-0147</span>
    <span><svg><use href="#i-mail"/></svg>hello@bellwetherhome.com</span>
    <span><svg><use href="#i-pin"/></svg>412 Alder Lane<br>Westbrook, Fairmont 00412</span>
  </div>
</section>

<section class="piece env-front">
  <div class="brand"><span class="brand-dot"></span><span>Bellwether<br>Home Inspections</span></div>
  <div class="wash" role="img" aria-label="Faint company watermark area"></div>
  <div class="note">lorem ipsumlorem ipsumlorem ipsumlorem ipsum lorem ipsum lorem ipsum</div>
</section>

<section class="piece env-back"><div class="flap"></div></section>

<section class="piece card-front">
  <div class="wash" role="img" aria-label="Faint company watermark area"></div>
  <div class="brand brand--light"><span class="brand-dot"></span><span>Bellwether<br>Home Inspections</span></div>
</section>

<section class="piece card-back">
  <div class="brand"><span class="brand-dot"></span><span>Bellwether<br>Home Inspections</span></div>
  <div class="wash" role="img" aria-label="Faint company watermark area"></div>
  <div class="name">MARCUS HALE</div>
  <div class="role">CEO</div>
  <div class="lines">
    <div><svg><use href="#i-phone"/></svg>407-555-0182</div>
    <div><svg><use href="#i-mail"/></svg>hello@bellwetherhome.com</div>
    <div><svg><use href="#i-pin"/></svg>412 Alder Lane<br>Westbrook, Fairmont 00412</div>
  </div>
</section>

</body>
</html>
```